Lebel for 500g Honey Jar

We want a design for a 500g honey bottle or Jar as shown in the attached image . All Requirement has been put in the attached brief document .
Also Logo and images have been uploaded . Feel free to play arround with the selected solor schemes .

Target Market(s)

Retail Market

Industry/Entity Type

FMCG

Colors
00AB8E
00BBA5
67D7C9
C6EFE9
E9F9F6
59FF00
82FF00
B8FF75
E3FFCB
F4FFEA
FFC000
F8CF3A
FAE287
FDF2CF
FEFAEE
F0912C
F2A743
F7CA91
FBE8D2
FDF5EE
EE7325
F08F49
F5BC92
FAE3D3
FDF4ED

Requirements
Must have
• The desing must contain the company Address, Logo , and Nutritional Facts
Nice to have
• Image of a honey Bee , see samples attahed

```html
<!DOCTYPE html>
<html lang="en">
<head>
<meta charset="utf-8">
<title>Meadowly Pure Honey – 500g Label</title>
<link href="https://fonts.googleapis.com/css2?family=Arimo:wght@400;700&display=swap" rel="stylesheet">
<style>
  :root {
    --backdrop: #f6ead2;
    --label: #f8cf5c;
    --label-edge: #f2c24a;
    --brand-ink: #1f1a14;
    --brand-dot: #6cc04a;
    --pure-orange: #ec8f1c;
    --honey-brown: #8a3f0a;
    --natural-green: #1f5a2a;
    --claim-orange: #e0841d;
    --footer-brown: #c0701a;
    --art-light: #fbd98a;
    --art-mid: #f2a743;
    --panel-bg: #fdf2cf;
    --panel-rule: #8a3f0a;
  }

  html, body {
    margin: 0;
    padding: 0;
    width: 816px;
    height: 1200px;
    overflow: hidden;
    background: var(--backdrop);
  }

  .canvas {
    position: relative;
    width: 816px;
    height: 1200px;
    font-family: "Arimo", Arial, sans-serif;
  }

  .label {
    position: absolute;
    left: 93px;
    top: 40px;
    width: 630px;
    height: 1120px;
    background: var(--label);
    border: 3px solid var(--label-edge);
    box-sizing: border-box;
    border-radius: 48% 48% 16% 16% / 24% 24% 7% 7%;
    overflow: hidden;
  }

  .brand {
    position: absolute;
    top: 150px;
    left: 0;
    right: 0;
    display: flex;
    justify-content: center;
    align-items: center;
    gap: 14px;
  }

  .brand-name {
    font-size: 78px;
    font-weight: 700;
    color: var(--brand-ink);
    letter-spacing: -1px;
    line-height: 1;
  }

  .brand-dot {
    width: 18px;
    height: 18px;
    border-radius: 50%;
    background: var(--brand-dot);
  }

  .product-kicker {
    position: absolute;
    top: 290px;
    left: 0;
    right: 0;
    text-align: center;
    font-size: 54px;
    font-weight: 700;
    color: var(--pure-orange);
    line-height: 1;
  }

  .product-name {
    position: absolute;
    top: 345px;
    left: 0;
    right: 0;
    margin: 0;
    text-align: center;
    font-size: 150px;
    font-weight: 700;
    color: var(--honey-brown);
    line-height: 1;
    letter-spacing: -2px;
  }

  .tagline {
    position: absolute;
    top: 500px;
    left: 0;
    right: 0;
    text-align: center;
    font-size: 33px;
    font-weight: 700;
    color: var(--natural-green);
  }

  .claims {
    position: absolute;
    top: 560px;
    left: 92px;
    font-size: 26px;
    color: var(--claim-orange);
    line-height: 1.3;
  }

  .claims p { margin: 0; }

  .hero-art {
    position: absolute;
    top: 640px;
    left: 30px;
    width: 320px;
    height: 240px;
    border-radius: 28px;
    background: radial-gradient(ellipse at 50% 60%, var(--art-mid) 0%, var(--art-light) 65%, var(--label) 100%);
  }

  .nutrition {
    position: absolute;
    top: 645px;
    left: 365px;
    width: 230px;
    box-sizing: border-box;
    padding: 8px 10px;
    background: var(--panel-bg);
    border: 2px solid var(--panel-rule);
    border-radius: 8px;
    color: var(--honey-brown);
    font-size: 14px;
    line-height: 1.2;
  }

  .nutrition-title {
    margin: 0 0 2px;
    font-size: 18px;
    font-weight: 700;
  }

  .nutrition-serving {
    margin: 0 0 4px;
    font-size: 12px;
    padding-bottom: 4px;
    border-bottom: 3px solid var(--panel-rule);
  }

  .nutrition table {
    width: 100%;
    border-collapse: collapse;
  }

  .nutrition td {
    padding: 3px 0;
    border-bottom: 1px solid var(--panel-rule);
  }

  .nutrition tr:last-child td { border-bottom: none; }

  .nutrition td:last-child {
    text-align: right;
    font-weight: 700;
  }

  .nutrition .sub { padding-left: 10px; }

  .packer {
    position: absolute;
    top: 905px;
    left: 0;
    right: 0;
    text-align: center;
    font-size: 28px;
    font-weight: 700;
    color: var(--footer-brown);
    line-height: 1.45;
  }

  .packer p { margin: 0; }

  .packer .address {
    font-size: 19px;
    font-weight: 400;
    line-height: 1.5;
  }
</style>
</head>
<body>
  <main class="canvas">
    <section class="label">
      <div class="brand">
        <span class="brand-name">meadowly</span>
        <span class="brand-dot"></span>
      </div>

      <div class="product-kicker">PURE</div>
      <h1 class="product-name">HONEY</h1>
      <div class="tagline">100% PURE &amp; NATURAL</div>

      <div class="claims">
        <p>0 Additive -&nbsp; 0 Preservative</p>
        <p>0 Colouring</p>
      </div>

      <div class="hero-art" role="img" aria-label="Illustration of a honey dipper dripping honey into a glass jar, a flying honey bee and a sunflower"></div>

      <div class="nutrition">
        <p class="nutrition-title">Nutrition Facts</p>
        <p class="nutrition-serving">Typical values per 100g</p>
        <table>
          <tr><td>Energy</td><td>1272kJ / 304kcal</td></tr>
          <tr><td>Fat</td><td>0g</td></tr>
          <tr><td>Carbohydrate</td><td>82g</td></tr>
          <tr><td class="sub">of which sugars</td><td>82g</td></tr>
          <tr><td>Protein</td><td>0.3g</td></tr>
          <tr><td>Sodium</td><td>4mg</td></tr>
        </table>
      </div>

      <div class="packer">
        <p>packed &amp; distributed by</p>
        <p>Amberfield farm limited</p>
        <p class="address">Plot 14, Meadow Lane, Clover Valley</p>
        <p>NET WT 500g</p>
      </div>
    </section>
  </main>
</body>
</html>
```